Business cards and stationery for Montessori school
Ridgeway Hollow Montessori
Business cards and stationery for Montessori school - Education
Creative Brief
Professional
Harpreet Malvik
Director
26415 48th Ave NE Kenmore WA 98094
425-613-PLAY (7529)
hmalvik@ridgewayhollowschool.org
www.ridgewayhollowschool.org
Need design for a good business card and stationary including letter heads and envelopes. Letter head should not have cell phone no. and email address should be info@ridgewayhollowschool.org.
Either enlarged logo or logo with school name and mission "Learning, Striving, Ascending".

```html
<!DOCTYPE html>
<html lang="en">
<head>
<meta charset="utf-8">
<title>Ridgeway Hollow Montessori – Business Card</title>
<link href="https://fonts.googleapis.com/css2?family=Montserrat:wght@600;700&family=Open+Sans:wght@400;600&display=swap" rel="stylesheet">
<style>
  :root {
    --backdrop: #d9d6d1;
    --card: #f7f7f5;
    --navy: #1f3d66;
    --ink: #3a3a3a;
    --muted: #6d6d6d;
    --accent: #1aa3e8;
  }
  * { box-sizing: border-box; margin: 0; padding: 0; }
  html, body {
    width: 1200px; height: 899px; overflow: hidden;
    background: var(--backdrop);
  }
  .stage {
    width: 1200px; height: 899px;
    display: flex; align-items: center; justify-content: center; gap: 48px;
  }
  .card {
    width: 520px; height: 300px;
    background: var(--card);
    border-radius: 30px;
    box-shadow: 0 14px 30px rgba(0,0,0,0.18);
    position: relative;
  }
  /* Contact side */
  .card--contact { display: flex; padding: 40px 36px; }
  .identity {
    width: 46%;
    display: flex; flex-direction: column; justify-content: space-between;
  }
  .person-name {
    font-family: "Montserrat", sans-serif; font-weight: 700;
    font-size: 15px; letter-spacing: 1px; color: var(--ink); text-transform: uppercase;
  }
  .person-title {
    font-family: "Open Sans", sans-serif; font-size: 10px;
    letter-spacing: 1px; color: var(--muted); text-transform: uppercase; margin-top: 4px;
  }
  .brand { display: flex; align-items: center; gap: 10px; }
  .brand__dot {
    flex: none; width: 34px; height: 34px; border-radius: 50%; background: var(--navy);
  }
  .brand__name {
    font-family: "Montserrat", sans-serif; font-weight: 700;
    color: var(--navy); text-transform: uppercase; line-height: 1.15;
    font-size: 14px; letter-spacing: 0.5px;
  }
  .contacts {
    width: 54%;
    display: flex; flex-direction: column; justify-content: center; gap: 16px;
    padding-left: 18px;
  }
  .contact-row { display: flex; align-items: center; gap: 12px; }
  .contact-icon {
    flex: none; width: 26px; height: 26px; border-radius: 5px;
    background: var(--accent); display: flex; align-items: center; justify-content: center;
  }
  .contact-text {
    font-family: "Open Sans", sans-serif; font-size: 10.5px;
    color: var(--ink); line-height: 1.4;
  }
  /* Logo side */
  .card--logo { display: flex; align-items: center; justify-content: center; }
  .card--logo .brand__dot { width: 54px; height: 54px; }
  .card--logo .brand__name { font-size: 22px; }
</style>
</head>
<body>
<main class="stage">
  <section class="card card--contact" aria-label="Business card, contact side">
    <div class="identity">
      <div>
        <p class="person-name">Harpreet Malvik</p>
        <p class="person-title">Director</p>
      </div>
      <div class="brand">
        <span class="brand__dot"></span>
        <p class="brand__name">Ridgeway Hollow<br>Montessori</p>
      </div>
    </div>
    <div class="contacts">
      <div class="contact-row">
        <span class="contact-icon">
          <svg width="14" height="14" viewBox="0 0 24 24"><path fill="#fff" d="M6.6 10.8a15 15 0 0 0 6.6 6.6l2.2-2.2c.3-.3.7-.4 1-.2 1.1.4 2.3.6 3.6.6.6 0 1 .4 1 1V20c0 .6-.4 1-1 1A17 17 0 0 1 3 4c0-.6.4-1 1-1h3.5c.6 0 1 .4 1 1 0 1.3.2 2.5.6 3.6.1.3 0 .7-.2 1z"/></svg>
        </span>
        <p class="contact-text">425-613-PLAY (7529)</p>
      </div>
      <div class="contact-row">
        <span class="contact-icon">
          <svg width="14" height="14" viewBox="0 0 24 24" fill="none" stroke="#fff" stroke-width="2"><circle cx="12" cy="12" r="9"/><path d="M3 12h18M12 3c3 3.5 3 14.5 0 18M12 3c-3 3.5-3 14.5 0 18"/></svg>
        </span>
        <p class="contact-text">www.ridgewayhollowschool.org</p>
      </div>
      <div class="contact-row">
        <span class="contact-icon">
          <svg width="14" height="14" viewBox="0 0 24 24" fill="none" stroke="#fff" stroke-width="2"><rect x="3" y="5" width="18" height="14" rx="1"/><path d="M3 6l9 7 9-7"/></svg>
        </span>
        <p class="contact-text">hmalvik@ridgewayhollowschool.org</p>
      </div>
      <div class="contact-row">
        <span class="contact-icon">
          <svg width="14" height="14" viewBox="0 0 24 24"><path fill="#fff" d="M12 2a7 7 0 0 0-7 7c0 5 7 13 7 13s7-8 7-13a7 7 0 0 0-7-7zm0 9.5A2.5 2.5 0 1 1 12 6.5a2.5 2.5 0 0 1 0 5z"/></svg>
        </span>
        <p class="contact-text">26415 48th Ave NE<br>Kenmore WA 98094</p>
      </div>
    </div>
  </section>

  <section class="card card--logo" aria-label="Business card, logo side">
    <div class="brand">
      <span class="brand__dot"></span>
      <p class="brand__name">Ridgeway Hollow<br>Montessori</p>
    </div>
  </section>
</main>
</body>
</html>
```